Geschäftspapier für Pfandhaus und Juwelier gesucht
Zielgruppe
Pfandhaus und Juwelier.
Aufgabenstellung
Ich betreibe mehrere Filialen und möchte all diese wir einem Briefkopf haben und ggf Platz für weitere da ich gerade 2 weitere eröffne. Unter www.leihhaus-Borlen.de sieht man Logo und Farben.
Ich möchte das Briefpapier als Datei haben und nicht gedruckt sondern will es selbst am Firmendrucker drucken.Die Bankverbindung sollte auch darauf sein aber erstmal etwas am Platzhalter eintragen .

```html
<!DOCTYPE html>
<html lang="de">
<head>
<meta charset="utf-8">
<title>Briefpapier – Tobias Borlen Pfandkredit</title>
<link rel="stylesheet" href="https://fonts.googleapis.com/css2?family=Open+Sans:wght@400;600;700&display=swap">
<style>
  :root {
    --gold: #b09a62;
    --charcoal: #4a4948;
    --ink: #1d1d1d;
    --paper: #ffffff;
    --backdrop: #e9e9ec;
    --fold: #bdbdbd;
  }
  * { box-sizing: border-box; margin: 0; padding: 0; }
  html, body {
    width: 1200px; height: 1010px; overflow: hidden;
    background: var(--backdrop);
    font-family: "Open Sans", Arial, sans-serif;
  }
  .sheet {
    position: absolute; left: 257px; top: 20px;
    width: 686px; height: 970px;
    background: var(--paper);
    box-shadow: 0 2px 10px rgba(0,0,0,.12);
    overflow: hidden;
  }
  .top-rule { position: absolute; left: 0; top: 0; width: 100%; height: 4px; background: var(--gold); }

  .brand-box {
    position: absolute; left: 54px; top: 4px; width: 246px; height: 150px;
    background: var(--charcoal);
  }
  .brand-frame {
    position: absolute; inset: 14px;
    border: 1px solid var(--gold);
    display: flex; align-items: center; justify-content: center;
  }
  .brand-name {
    color: var(--gold); font-weight: 600; font-size: 21px; letter-spacing: .5px;
    text-align: center; line-height: 1.25;
  }

  .return-line {
    position: absolute; left: 58px; top: 176px;
    font-size: 7px; color: var(--ink);
    border-bottom: .8px solid var(--ink); padding-bottom: 1px;
  }
  .recipient {
    position: absolute; left: 66px; top: 196px;
    font-size: 11px; line-height: 14px; color: var(--ink); font-style: normal;
  }

  .fold-mark { position: absolute; left: 0; width: 18px; height: 1px; background: var(--fold); }
  .fold-1 { top: 343px; }
  .fold-2 { top: 686px; }

  .branches { position: absolute; left: 440px; top: 26px; width: 220px; }
  .branches-title {
    color: var(--gold); font-weight: 700; font-size: 8.5px; letter-spacing: .2px;
    margin-bottom: 6px;
  }
  .branch-list {
    border-left: 1px solid var(--gold); padding-left: 12px; padding-bottom: 6px;
    list-style: none;
  }
  .branch { font-size: 8px; line-height: 10.5px; color: var(--ink); margin-bottom: 9px; }
  .branch:last-child { margin-bottom: 0; }
  .contact { display: flex; align-items: center; gap: 6px; padding-left: 4px; }
  .contact svg { width: 8px; height: 8px; fill: var(--gold); flex: none; }

  .footer-band { position: absolute; left: 0; bottom: 0; width: 686px; height: 46px; }
  .footer-info {
    position: absolute; left: 40px; bottom: 7px;
    display: flex; align-items: center; gap: 12px;
    color: var(--paper); font-size: 8.5px; line-height: 11px;
  }
  .footer-info .divider { width: 1px; height: 22px; background: var(--paper); opacity: .8; }
  .website {
    position: absolute; left: 480px; bottom: 14px; width: 156px;
    text-align: center; white-space: nowrap;
    color: var(--paper); font-size: 10.5px; letter-spacing: .1px;
  }
</style>
</head>
<body>
<svg width="0" height="0" style="position:absolute">
  <symbol id="icon-phone" viewBox="0 0 10 10">
    <path d="M2.2 .6 3.6 2.4 2.8 3.4c.6 1.4 1.8 2.6 3.2 3.2l1-.8 1.8 1.4-.9 1.6C4.4 8.6 1.2 5.4.6 1.6Z"/>
  </symbol>
  <symbol id="icon-fax" viewBox="0 0 10 10">
    <rect x="2.5" y="0.8" width="5" height="3"/>
    <rect x="0.8" y="3.6" width="8.4" height="4" rx=".6"/>
    <rect x="2.5" y="6.4" width="5" height="2.8"/>
  </symbol>
  <symbol id="icon-mail" viewBox="0 0 10 10">
    <path d="M.6 2.2h8.8v5.6H.6Z M.9 2.4 5 5.6l4.1-3.2"/>
  </symbol>
</svg>

<main class="sheet">
  <div class="top-rule"></div>

  <div class="brand-box">
    <div class="brand-frame">
      <p class="brand-name">Tobias Borlen<br>Pfandkredit</p>
    </div>
  </div>

  <p class="return-line">Tobias Borlen Pfandkredit&nbsp;|&nbsp;Lindenallee 4&nbsp;|&nbsp;66111 Saarbrücken</p>

  <address class="recipient">
    Herr<br>Mark Mustermann<br>Musterweg 13<br>24102 Dortmund
  </address>

  <span class="fold-mark fold-1"></span>
  <span class="fold-mark fold-2"></span>

  <section class="branches">
    <h2 class="branches-title">TOBIAS BORLEN PFANDKREDIT</h2>
    <ul class="branch-list">
      <li class="branch">
        Lindenallee 4<br>66111 Saarbrücken
        <div class="contact"><svg><use href="#icon-phone"/></svg>+49 (0) 681 5550123-0</div>
        <div class="contact"><svg><use href="#icon-fax"/></svg>+49 (0) 681 5550123-9</div>
        <div class="contact"><svg><use href="#icon-mail"/></svg>sb@leihhaus-borlen.de</div>
      </li>
      <li class="branch">
        Gartenstraße 7<br>54290 Trier
        <div class="contact"><svg><use href="#icon-phone"/></svg>+49 (0) 651 5550456-5</div>
        <div class="contact"><svg><use href="#icon-fax"/></svg>+49 (0) 651 5550456-0</div>
        <div class="contact"><svg><use href="#icon-mail"/></svg>tr@leihhaus-borlen.de</div>
      </li>
      <li class="branch">
        Marktweg 21<br>55116 Mainz
        <div class="contact"><svg><use href="#icon-phone"/></svg>+49 (0) 6131 5550780</div>
        <div class="contact"><svg><use href="#icon-fax"/></svg>+49 (0) 6131 5550788</div>
        <div class="contact"><svg><use href="#icon-mail"/></svg>mz@leihhaus-borlen.de</div>
      </li>
      <li class="branch">
        Uferstraße 52<br>65185 Wiesbaden
        <div class="contact"><svg><use href="#icon-phone"/></svg>+49 (0) 611 5550312</div>
        <div class="contact"><svg><use href="#icon-fax"/></svg>+49 (0) 611 5550319</div>
        <div class="contact"><svg><use href="#icon-mail"/></svg>wi@leihhaus-borlen.de</div>
      </li>
      <li class="branch">
        Parkstr. 6<br>67655 Kaiserslautern
        <div class="contact"><svg><use href="#icon-phone"/></svg>+49 (0) 0631 5550640</div>
        <div class="contact"><svg><use href="#icon-mail"/></svg>kl@leihhaus-borlen.de</div>
      </li>
    </ul>
  </section>

  <svg class="footer-band" viewBox="0 0 686 46" preserveAspectRatio="none">
    <polygon points="0,6 474,6 466,46 0,46" fill="var(--gold)"/>
    <polygon points="482,0 642,0 632,46 472,46" fill="var(--charcoal)"/>
    <polygon points="656,6 686,6 686,46 648,46" fill="var(--gold)"/>
  </svg>

  <footer class="footer-info">
    <p>Bankverbindung:<br>Tobias Borlen</p>
    <span class="divider"></span>
    <p>Westhafen Bank<br>USt-ID-Nr. DEXXXXXXXXX</p>
    <span class="divider"></span>
    <p>IBAN: DEXX XXXX XXXX XXXX XXXX X<br>BIC: XXXXXXXX</p>
  </footer>
  <p class="website">www.leihhaus-Borlen.de</p>
</main>
</body>
</html>
```